Web site design for news feed - Korvel Live

We need to design a webpage to promote our web scraping newsfeed (similar to pagewhirl) the name of the business is "Korvel Live" ( a subsidiary of our company Korvel - see www.korvel-holdings-example.com for details, DO NOT BASE THAT WEBSITE ON YOUR DESIGN).

We are inspired by famous Economists, we are inspired by empirical data, accuracy, but importantly the site needs to portray our "new approach" to delivering functional and "boring" financial news flow (pagewhirl)

Websites we like:

www.zentrip-example.com - love the graphics
www.pagewhirl-example.com - love the functionality
http://www.marketdial-example.com/ - practical
http://www.wirepost-example.com/ - practical
http://www.quorvantsoft-example.com/en-us/default.aspx
www.tkx-example.com
http://www.harborledger-example.com/
www.strydo-example.com

Our logo is attached

We like black and white, artful, lyle denholm etc
Updates

Hi All, please bear in mind that this is a NEWS site (it will need space to post stories) - so whilst the visual aspect is really important, the functionally around the amount of stories we can post is important too.

think marketdial-example.com, www.quillbrook-example.com, www.tkx-example.com - but feel (creativity) is zentrip-example.com, pagewhirl-example.com

thanks all for some great designs.

i will revert to those closest tomorrow.
in the meantime, please bear in mind that the vision of skylines and economists helps me get to the design immediately, it resonates better, it helps me visually decide. 
lastly, in terms of the news "spaces", i will need to have 6 "top stories" and then room for maybe 20 more headlines..the top stories will need a picture, the 20 others will not (just headline text).
Thanks everyone again

Industry/Entity Type

Financial

Font styles to use
Serif
Sans Serif

```html
<!DOCTYPE html>
<html lang="en">
<head>
<meta charset="utf-8">
<title>Korvel Live — News Feed</title>
<link rel="stylesheet" href="https://fonts.googleapis.com/css2?family=Lato:wght@300;400;700;900&display=swap">
<style>
:root{
  --orange:#f7861e;
  --black:#000;
  --topbar:#1f1f1f;
  --footer:#1a1a1a;
  --caption:#d9d9d9;
  --caption-text:#555;
  --band:#dcdcdc;
  --white:#fff;
  --muted:#9a9a9a;
}
*{box-sizing:border-box;margin:0;padding:0}
html,body{width:1200px;height:2326px;overflow:hidden;background:var(--white);font-family:'Lato',Arial,sans-serif}
.page{position:relative;width:1200px;height:2326px}
.abs{position:absolute}

/* top bar */
.topbar{left:0;top:0;width:1200px;height:58px;background:var(--topbar)}
.social{display:flex;gap:24px}
.social span{width:22px;height:22px;border-radius:50%;background:var(--white);display:block}
.topbar .social{position:absolute;left:135px;top:18px}
.account{left:717px;top:20px;color:var(--white);font-size:14px;letter-spacing:.5px}
.account b{font-weight:400;margin:0 8px;color:var(--muted)}
.search{left:862px;top:16px;width:220px;height:30px;display:flex}
.search .field{flex:1;background:#555;color:var(--white);font-size:15px;padding:6px 8px}
.search .go{width:28px;background:var(--orange);display:flex;align-items:center;justify-content:center}

/* header */
.header{left:0;top:58px;width:1200px;height:136px;background:var(--black)}
.brand{display:flex;align-items:center;gap:14px;color:#bdbdbd;font-weight:300;font-size:38px;line-height:40px}
.brand i{width:42px;height:42px;background:var(--orange);display:block}
.header .brand{position:absolute;left:116px;top:26px}
.brand .name{width:150px}
.nav{position:absolute;left:372px;top:0;display:flex;height:136px;align-items:center;font-size:18px;color:var(--white)}
.nav a{color:var(--white);text-decoration:none;display:flex;align-items:center;height:136px}
.nav .home{background:var(--orange);width:93px;justify-content:center;margin-right:23px}
.nav .item{margin-right:26px}
.nav svg{margin-left:8px}

/* hero */
.hero{left:0;top:194px;width:1200px;height:548px;background:radial-gradient(ellipse at 50% 40%,#7a7a7a 0%,#4a4a4a 55%,#222 100%)}
.hero-arrow{top:262px}
.hero-title{left:0;top:340px;width:1200px;text-align:center;color:var(--white);font-size:33px;line-height:43px;font-weight:400}
.hero-btn{left:521px;top:454px;width:136px;height:36px;background:var(--orange);color:var(--white);font-size:13px;display:flex;align-items:center;justify-content:center;letter-spacing:.3px}
.dots-band{left:0;top:742px;width:1200px;height:53px;background:var(--band)}
.dots{position:absolute;left:552px;top:20px;display:flex;gap:9px}
.dots span{width:10px;height:10px;border-radius:50%;background:#222}
.dots .on{background:var(--orange)}

/* news */
.news-head{left:108px;top:833px;width:980px;height:72px;background:var(--black);color:var(--white);font-size:25px;font-weight:700;padding:20px 26px}
.news-notch{left:148px;top:904px}
.filters{left:108px;top:952px;display:flex;gap:13px}
.filters span{height:37px;background:var(--black);color:var(--white);font-size:17px;display:flex;align-items:center;justify-content:center}
.filters .on{background:var(--orange)}

.card{position:absolute;background:var(--caption)}
.card .photo{position:absolute;left:0;top:0;width:100%;border-bottom:4px solid var(--orange)}
.card .cap{position:absolute;left:14px;right:10px}
.card h3{font-size:17px;line-height:20px;font-weight:700;color:var(--caption-text);text-transform:uppercase}
.meta{font-size:9px;color:#666;margin-top:5px;display:flex;align-items:center;gap:5px}
.feature{background:var(--orange)}
.feature h3{color:var(--white)}
.feature .meta{color:var(--white)}
.feature p{font-size:10px;line-height:14px;color:#ffe0c2;margin-top:8px}
.readmore{position:absolute;left:144px;top:80px;width:136px;height:44px;border:2px solid var(--white);color:var(--white);font-size:21px;display:flex;align-items:center;justify-content:center;background:rgba(0,0,0,.35)}
.share{position:absolute;right:14px;top:10px;display:flex;gap:6px}
.share span{width:22px;height:22px;border-radius:50%;background:var(--white)}

/* newsletter */
.newsletter{left:0;top:2070px;width:1200px;height:76px;background:var(--orange)}
.newsletter .label{position:absolute;left:176px;top:25px;color:var(--white);font-weight:700;font-size:17px}
.newsletter .input{position:absolute;left:457px;top:24px;width:481px;height:35px;background:var(--white);color:#aaa;font-size:16px;padding:7px 10px}
.newsletter .submit{position:absolute;left:938px;top:24px;width:99px;height:35px;background:var(--black);color:var(--white);font-size:22px;display:flex;align-items:center;justify-content:center}

/* footer */
.footer{left:0;top:2146px;width:1200px;height:180px;background:var(--footer)}
.footer .brand{position:absolute;left:116px;top:42px}
.footer .social{position:absolute;left:455px;top:78px}
.contact{position:absolute;left:866px;top:30px;color:var(--white)}
.contact h4{font-size:17px;font-weight:400;letter-spacing:.5px;margin-bottom:14px}
.contact li{list-style:none;display:flex;gap:10px;font-size:12px;color:#bbb;line-height:17px;margin-bottom:8px}
.contact svg{flex:none;margin-top:2px}
</style>
</head>
<body>
<div class="page">

  <div class="abs topbar">
    <div class="social"><span></span><span></span><span></span><span></span><span></span><span></span></div>
    <div class="abs account">LOGIN<b>|</b>SIGN UP</div>
    <div class="abs search">
      <div class="field">Search</div>
      <div class="go"><svg width="14" height="14" viewBox="0 0 14 14"><circle cx="6" cy="6" r="4" fill="none" stroke="#fff" stroke-width="2"/><line x1="9" y1="9" x2="13" y2="13" stroke="#fff" stroke-width="2"/></svg></div>
    </div>
  </div>

  <header class="abs header">
    <div class="brand"><i></i><span class="name">Korvel Live</span></div>
    <nav class="nav">
      <a class="home">Home</a>
      <a class="item">News Feed<svg width="14" height="8" viewBox="0 0 14 8"><path d="M1 1l6 6 6-6" fill="none" stroke="#fff" stroke-width="1.5"/></svg></a>
      <a class="item">Community<svg width="14" height="8" viewBox="0 0 14 8"><path d="M1 1l6 6 6-6" fill="none" stroke="#fff" stroke-width="1.5"/></svg></a>
      <a class="item">Support<svg width="14" height="8" viewBox="0 0 14 8"><path d="M1 1l6 6 6-6" fill="none" stroke="#fff" stroke-width="1.5"/></svg></a>
      <a class="item">Contact</a>
    </nav>
  </header>

  <section class="abs hero" role="img" aria-label="Black and white photograph of a crowded trading floor">
    <svg class="abs hero-arrow" style="left:24px" width="18" height="30" viewBox="0 0 18 30"><path d="M16 2L3 15l13 13" fill="none" stroke="#fff" stroke-width="2"/></svg>
    <svg class="abs hero-arrow" style="right:24px" width="18" height="30" viewBox="0 0 18 30"><path d="M2 2l13 13L2 28" fill="none" stroke="#fff" stroke-width="2"/></svg>
    <h1 class="abs hero-title">Korvel leverages technology and data analytic<br>to cut through the noise of daily investment advice</h1>
    <div class="abs hero-btn">READ MORE</div>
  </section>
  <div class="abs dots-band"><div class="dots"><span class="on"></span><span></span><span></span><span></span><span></span></div></div>

  <h2 class="abs news-head">News</h2>
  <svg class="abs news-notch" width="24" height="26" viewBox="0 0 24 26"><path d="M0 0h24L2 26z" fill="#000"/></svg>
  <div class="abs filters">
    <span class="on" style="width:86px">All</span>
    <span style="width:101px">Latest</span>
    <span style="width:103px">Top 10</span>
    <span style="width:105px">Finance</span>
    <span style="width:121px">Investment</span>
    <span style="width:93px">Research</span>
  </div>

  <article class="card" style="left:108px;top:1066px;width:320px;height:272px">
    <div class="photo" role="img" aria-label="Stock exchange ticker board with market prices" style="height:194px;background:linear-gradient(135deg,#2a2a2a,#6a6a6a 60%,#3a3a3a)"></div>
    <div class="cap" style="top:208px"><h3>Ut tempor mi nec consequat</h3><div class="meta">by John Doe <svg width="9" height="8" viewBox="0 0 9 8"><path d="M4.5 8L0 3.5A2 2 0 0 1 4.5 1a2 2 0 0 1 4.5 2.5z" fill="#555"/></svg> 19</div></div>
  </article>

  <article class="card feature" style="left:436px;top:1008px;width:407px;height:330px">
    <div class="photo" role="img" aria-label="Hand using a tablet showing financial charts" style="height:194px;border-bottom:none;background:linear-gradient(160deg,#1e1e1e,#7c7c7c 55%,#444)">
      <div class="share"><span></span><span></span></div>
      <div class="readmore">Readmore</div>
    </div>
    <div class="cap" style="top:206px;left:18px;right:18px"><h3>Neque porro quisquam est qui dolorem</h3><div class="meta">by John Doe <svg width="9" height="8" viewBox="0 0 9 8"><path d="M4.5 8L0 3.5A2 2 0 0 1 4.5 1a2 2 0 0 1 4.5 2.5z" fill="#fff"/></svg> 19</div>
      <p>Suspendisse luctus risus sed sagittis vestibulum. Nullam eget turpis eu felis semper hendrerit sit amet nec turpis. Proin pharetra dolor non ligula elementum.</p></div>
  </article>

  <article class="card" style="left:849px;top:1066px;width:239px;height:272px">
    <div class="photo" role="img" aria-label="Businessman in a dark suit, seen from the side" style="height:190px;background:linear-gradient(120deg,#bdbdbd,#5a5a5a 60%,#2c2c2c)"></div>
    <div class="cap" style="top:204px"><h3>Donec vulputate vehicula</h3><div class="meta">by John Doe <svg width="9" height="8" viewBox="0 0 9 8"><path d="M4.5 8L0 3.5A2 2 0 0 1 4.5 1a2 2 0 0 1 4.5 2.5z" fill="#555"/></svg> 19</div></div>
  </article>

  <article class="card" style="left:108px;top:1345px;width:237px;height:438px">
    <div class="photo" role="img" aria-label="Businesswoman seated on a sofa working on a laptop" style="height:351px;background:linear-gradient(180deg,#e8e8e8,#9a9a9a 60%,#5a5a5a)"></div>
    <div class="cap" style="top:365px"><h3>Cum sociis natoque penatibus</h3><div class="meta">by John Doe <svg width="9" height="8" viewBox="0 0 9 8"><path d="M4.5 8L0 3.5A2 2 0 0 1 4.5 1a2 2 0 0 1 4.5 2.5z" fill="#555"/></svg> 19</div></div>
  </article>

  <article class="card" style="left:353px;top:1345px;width:324px;height:276px">
    <div class="photo" role="img" aria-label="Business partners shaking hands across a table" style="height:202px;background:linear-gradient(135deg,#d6d6d6,#8a8a8a 55%,#4a4a4a)"></div>
    <div class="cap" style="top:216px"><h3>Vivamus massa risus</h3><div class="meta">by John Doe <svg width="9" height="8" viewBox="0 0 9 8"><path d="M4.5 8L0 3.5A2 2 0 0 1 4.5 1a2 2 0 0 1 4.5 2.5z" fill="#555"/></svg> 19</div></div>
  </article>

  <article class="card" style="left:684px;top:1345px;width:404px;height:438px">
    <div class="photo" role="img" aria-label="Team of business people seated at a meeting table" style="height:351px;background:linear-gradient(135deg,#d0d0d0,#6e6e6e 55%,#2e2e2e)"></div>
    <div class="cap" style="top:365px"><h3>Etiam lobortis porttitor elit vel feugiat.</h3><div class="meta">by John Doe <svg width="9" height="8" viewBox="0 0 9 8"><path d="M4.5 8L0 3.5A2 2 0 0 1 4.5 1a2 2 0 0 1 4.5 2.5z" fill="#555"/></svg> 19</div></div>
  </article>

  <article class="card" style="left:108px;top:1791px;width:237px;height:264px">
    <div class="photo" role="img" aria-label="Thoughtful businessman portrait" style="height:182px;background:linear-gradient(135deg,#3a3a3a,#7a7a7a 55%,#2a2a2a)"></div>
    <div class="cap" style="top:196px"><h3>Curabitur ac mauris</h3><div class="meta">by John Doe <svg width="9" height="8" viewBox="0 0 9 8"><path d="M4.5 8L0 3.5A2 2 0 0 1 4.5 1a2 2 0 0 1 4.5 2.5z" fill="#555"/></svg> 19</div></div>
  </article>

  <article class="card" style="left:353px;top:1628px;width:324px;height:427px">
    <div class="photo" role="img" aria-label="Portrait of a smiling senior businessman" style="height:345px;background:linear-gradient(180deg,#5a5a5a,#a8a8a8 45%,#3a3a3a)"></div>
    <div class="cap" style="top:359px"><h3>Neque porro quisquam est qui dolorem</h3><div class="meta">by John Doe <svg width="9" height="8" viewBox="0 0 9 8"><path d="M4.5 8L0 3.5A2 2 0 0 1 4.5 1a2 2 0 0 1 4.5 2.5z" fill="#555"/></svg> 19</div></div>
  </article>

  <article class="card" style="left:684px;top:1791px;width:404px;height:264px">
    <div class="photo" role="img" aria-label="Businesswoman with glasses talking on a phone" style="height:182px;background:linear-gradient(135deg,#1e1e1e,#6a6a6a 50%,#2a2a2a)"></div>
    <div class="cap" style="top:196px"><h3>Aenean leo metus, accumsan sit amet</h3><div class="meta">by John Doe <svg width="9" height="8" viewBox="0 0 9 8"><path d="M4.5 8L0 3.5A2 2 0 0 1 4.5 1a2 2 0 0 1 4.5 2.5z" fill="#555"/></svg> 19</div></div>
  </article>

  <section class="abs newsletter">
    <div class="label">SUBSCRIBE OUR NEWSETTER</div>
    <div class="input">email address</div>
    <div class="submit">submit</div>
  </section>

  <footer class="abs footer">
    <div class="brand"><i></i><span class="name">Korvel Live</span></div>
    <div class="social"><span></span><span></span><span></span><span></span><span></span><span></span></div>
    <div class="contact">
      <h4>CONTACT</h4>
      <ul>
        <li><svg width="12" height="14" viewBox="0 0 12 14"><path d="M6 14S1 8 1 5a5 5 0 0 1 10 0c0 3-5 9-5 9z" fill="#f7861e"/><circle cx="6" cy="5" r="2" fill="#1a1a1a"/></svg><span>4567 Street name,<br>012 12 City name, Country</span></li>
        <li><svg width="12" height="10" viewBox="0 0 12 10"><rect width="12" height="10" fill="#f7861e"/><path d="M0 0l6 5 6-5" fill="none" stroke="#1a1a1a" stroke-width="1.2"/></svg><span>mail@korvellive-example.com</span></li>
        <li><svg width="12" height="12" viewBox="0 0 12 12"><circle cx="6" cy="6" r="6" fill="#f7861e"/><path d="M0 6h12M6 0c-3 3-3 9 0 12M6 0c3 3 3 9 0 12" fill="none" stroke="#1a1a1a" stroke-width="1"/></svg><span>www.korvellive-example.com</span></li>
      </ul>
    </div>
  </footer>

</div>
</body>
</html>
```